Brantley Advisory Group provides support for renewable energy projects to utilities and suppliers

I need a professional looking business card that is both simple and elegant and unique. My clients are mostly large organizations not individuals. I am a consultant with my own company that is small but would like to give clients the impression I am larger. Smart grid, fiber optics, software, field hardware, distribution automation, substation automation, operations, energy storage/batteries, microgrids, customer service, strategy/roadmaps, conservation, Automated Metering Infrastruture (AMI or smart meters) are all areas of focus.

Target Market(s)

Utilities, suppliers, governmental agencies involved in energy. All types of energy especially natural gas and electrical. Especially renewable energy or green projects.

Contact Information for Business Card

Name - Tobin Halvery Cell Phone - 425.318.2746 Email - mbrantley@brantleyag-example.com
Company - Brantley Advisory Group (logo) Title - Principal

Font styles to use
Serif
Sans Serif

Colors

Designer to choose colors to be used in the design.

Requirements
Must have
• Simple and professional and powerful.
• Unique/creative design.
Nice to have
• Utilize color scheme to accent logo colors. Maybe some geometric pattern on edge of card with color.
Should not have
• Busy, complicated, traditional

```html
<!DOCTYPE html>
<html lang="en">
<head>
<meta charset="utf-8">
<title>Brantley Advisory Group – Business Card</title>
<link rel="stylesheet" href="https://fonts.googleapis.com/css2?family=Josefin+Sans:wght@300;400;600&display=swap">
<style>
  :root {
    --backdrop: #4670b0;
    --front-light: #e4e2f2;
    --front-mid: #d2d0e6;
    --front-shade: #b9b6d0;
    --brand-blue: #2b3a9f;
    --back-deep: #28339a;
    --back-glow: #3646b4;
    --ink-light: #ffffff;
    --ink-soft: #dfe3ff;
  }
  * { margin: 0; padding: 0; box-sizing: border-box; }
  html, body {
    width: 1200px;
    height: 800px;
    overflow: hidden;
    background: var(--backdrop);
    font-family: "Josefin Sans", sans-serif;
  }
  .canvas {
    position: relative;
    width: 1200px;
    height: 800px;
  }
  .card {
    position: absolute;
    top: 284px;
    width: 428px;
    height: 238px;
    overflow: hidden;
  }
  .card--front { left: 111px; }
  .card--back { left: 638px; }

  /* Front side */
  .front-texture {
    position: absolute;
    inset: 0;
    background:
      radial-gradient(ellipse 60% 70% at 35% 55%, var(--front-light) 0%, transparent 75%),
      linear-gradient(135deg, var(--front-mid) 0%, var(--front-light) 45%, var(--front-shade) 100%);
  }
  .brand-lockup {
    position: absolute;
    left: 0;
    right: 0;
    top: 96px;
    display: flex;
    align-items: center;
    justify-content: center;
    gap: 12px;
  }
  .brand-mark {
    width: 26px;
    height: 26px;
    border: 3px solid var(--brand-blue);
    border-radius: 3px;
  }
  .brand-name {
    font-weight: 600;
    font-size: 24px;
    color: var(--brand-blue);
    letter-spacing: 0.5px;
    padding-top: 4px;
  }

  /* Back side */
  .card--back {
    background:
      linear-gradient(90deg, var(--back-deep) 0%, var(--back-glow) 38%, var(--back-deep) 62%, var(--back-deep) 100%);
  }
  .name-row {
    position: absolute;
    left: 108px;
    top: 105px;
    display: flex;
    align-items: center;
    color: var(--ink-light);
  }
  .person-name {
    font-weight: 600;
    font-size: 24px;
    font-variant: small-caps;
    letter-spacing: 1px;
    padding-top: 4px;
  }
  .name-divider {
    width: 1px;
    height: 34px;
    background: var(--ink-light);
    margin: 0 8px;
  }
  .person-title {
    font-weight: 600;
    font-size: 12px;
    letter-spacing: 0.5px;
    padding-top: 8px;
  }
  .contact {
    position: absolute;
    left: 14px;
    top: 179px;
    padding-left: 7px;
    border-left: 1px solid var(--ink-soft);
    color: var(--ink-soft);
    font-weight: 300;
    font-size: 10px;
  }
  .contact-line {
    display: flex;
    align-items: center;
    gap: 5px;
    height: 18px;
  }
  .contact-icon { width: 12px; height: 12px; flex: none; }
</style>
</head>
<body>
<main class="canvas">
  <section class="card card--front" aria-label="Card front">
    <div class="front-texture" role="img" aria-label="Soft lavender tiled texture background"></div>
    <div class="brand-lockup">
      <span class="brand-mark"></span>
      <span class="brand-name">Brantley Advisory Group</span>
    </div>
  </section>

  <section class="card card--back" aria-label="Card back">
    <div class="name-row">
      <span class="person-name">Tobin Halvery</span>
      <span class="name-divider"></span>
      <span class="person-title">PRINCIPAL</span>
    </div>
    <div class="contact">
      <div class="contact-line">
        <svg class="contact-icon" viewBox="0 0 12 12" fill="none" stroke="currentColor" stroke-width="1">
          <rect x="0.5" y="2.5" width="11" height="8" rx="0.5"/>
          <polyline points="0.5,2.5 6,7 11.5,2.5"/>
        </svg>
        <span>mbrantley@brantleyag-example.com</span>
      </div>
      <div class="contact-line">
        <svg class="contact-icon" viewBox="0 0 12 12" fill="none" stroke="currentColor" stroke-width="1">
          <rect x="3" y="1.5" width="6" height="10" rx="1"/>
          <line x1="5" y1="9.5" x2="7" y2="9.5"/>
          <rect x="4.2" y="3" width="3.6" height="3"/>
        </svg>
        <span>425.318.2746</span>
      </div>
    </div>
  </section>
</main>
</body>
</html>
```